Marigold Covenant - lifestyle coaching for women looking for D/s dynamic

Create website design and logo based on the requirements in the creative brief file.

Executive summary:
Company Info
Marigold Covenant is a new life and intimacy coaching company founded by a life and fitness coach. The company focuses on integrating power exchange dynamics into intimate relationships, based on the founder’s personal journey.

Product
The company offers subscription-based online coaching programs with online class structure provided through a learning management system.
Customer Profile
• Target Audience: Women aged 45-55
• Customer needs: see appendix 1
• Language: English-speaking
• Economic Status: Middle to upper class
• Device Usage: Predominantly mobile (iOS and Android)

Target Market(s)

• Target Audience: Women aged 45-55 • Customer needs: see appendix 1 • Language: English-speaking • Economic Status: Middle to upper class • Device Usage: Predominantly mobile (iOS and Android)

Industry/Entity Type

Personal Development / Lifestyle Coaching

Coding

Coded - Design and coding required

Number of Pages Required

1 page

Font styles to use
Sans Serif

Requirements
Must have
• Lead capture tools, scheduling of intake calls, payment via Stripe, ready to be maintained by WIX or Wordpress
Nice to have
• Blog page

```html
<!DOCTYPE html>
<html lang="en">
<head>
<meta charset="utf-8">
<title>Marigold Covenant – Life and Intimacy Coaching</title>
<link href="https://fonts.googleapis.com/css2?family=Poppins:wght@400;500;600;700&family=Great+Vibes&display=swap" rel="stylesheet">
<style>
:root{
  --beige:#e9d3ba;
  --beige-soft:#f1e2d1;
  --purple:#5c2b4b;
  --teal:#3b5e5f;
  --ink:#1d1d1d;
  --grey:#6f6f6f;
  --muted:#8a8a8a;
  --white:#ffffff;
}
*{margin:0;padding:0;box-sizing:border-box}
html,body{width:1200px;height:4306px;overflow:hidden;background:var(--white)}
body{position:relative;font-family:'Poppins',sans-serif;color:var(--ink)}
.abs{position:absolute}
.btn{position:absolute;display:flex;align-items:center;justify-content:center;background:var(--purple);color:var(--white);border-radius:40px;font-weight:400;text-decoration:none}
.accent{color:var(--teal)}

/* hero */
.hero{left:0;top:0;width:1200px;height:710px;background:linear-gradient(90deg,#e6cdb1,#ecd8c2 55%,#e4cbb0)}
.hero-wave{left:0;top:560px;width:1200px;height:160px}
.brand-badge{left:87px;top:24px;width:106px;height:106px;border-radius:50%;background:var(--teal);border:4px solid var(--purple);display:flex;align-items:center;justify-content:center;text-align:center;color:var(--white);font-size:9px;font-weight:600;line-height:1.2;padding:10px}
.nav{left:0;top:68px;width:1200px;font-size:13px;color:#2c2c2c}
.nav span{position:absolute;transform:translateX(-50%)}
.nav-cta{left:964px;top:63px;width:151px;height:31px;font-size:11px}
.hero-title{left:154px;top:250px;width:460px;font-size:32px;font-weight:600;line-height:38px;color:#6a6762;letter-spacing:.3px}
.hero-cta{left:154px;top:399px;width:175px;height:34px;font-size:12px}
.hero-arrow{width:24px;height:30px}
.hero-photo{left:708px;top:169px;width:338px;height:338px;border-radius:50%;background:radial-gradient(circle at 45% 35%,#f7d7b4,#e2a47d 55%,#b4768a)}

/* services */
.section-title{position:absolute;left:0;width:1200px;text-align:center;font-size:40px;font-weight:600;letter-spacing:.3px}
.service{position:absolute;width:250px;text-align:center;transform:translateX(-50%)}
.service-icon{width:90px;height:90px;margin:0 auto;border-radius:50%;background:var(--teal);border:5px solid #dfe6e6;display:flex;align-items:center;justify-content:center}
.service h3{margin-top:26px;font-size:12.5px;font-weight:600;color:var(--ink)}
.service p{margin-top:8px;font-size:11.5px;line-height:17px;color:var(--muted)}

/* about */
.about-frame{left:72px;top:1434px;width:205px;height:184px;background:var(--beige)}
.about-photo{left:92px;top:1208px;width:394px;height:393px;border-radius:160px 0 160px 0;background:linear-gradient(180deg,#c9d3da,#aebac2 55%,#7f8b5e 80%,#5f6a44)}
.about-title{left:615px;top:1266px;font-size:40px;font-weight:600}
.about-text{left:613px;top:1334px;width:460px;font-size:15.5px;line-height:26.5px;color:var(--grey)}
.about-cta{left:615px;top:1507px;width:187px;height:50px;font-size:19px}

/* featured */
.featured{left:0;top:1738px;width:1200px;height:423px;background:radial-gradient(ellipse at 55% 60%,#d8c2a8,#e4cfb6 45%,#e9d5be)}
.featured-title{top:1828px}
.featured-sub{left:260px;top:1888px;width:680px;text-align:center;font-size:16px;line-height:28px;color:#8d857c}
.phone-circle{left:180px;top:1975px;width:88px;height:88px;border-radius:50%;background:var(--purple);display:flex;align-items:center;justify-content:center}
.help-label{left:284px;top:1986px;font-size:21px;color:#2c2c2c}
.help-call{left:284px;top:2017px;font-size:29px;font-weight:600;color:var(--white)}
.or-word{left:595px;top:1960px;font-family:'Great Vibes',cursive;font-size:96px;color:var(--white);line-height:1}
.featured-cta{left:740px;top:1992px;width:276px;height:68px;font-size:20px}

/* benefits */
.benefits-title{top:2280px}
.benefits-sub{left:290px;top:2350px;width:620px;text-align:center;font-size:15.5px;line-height:26px;color:var(--grey)}
.benefits-photo{left:672px;top:2503px;width:396px;height:543px;border-radius:140px 0 140px 0;background:linear-gradient(180deg,#cfd5db,#b9c1c8 60%,#a29a6e 85%,#857a4c)}
.benefit{position:absolute;left:104px;width:590px;height:58px;background:var(--white);border-radius:30px;box-shadow:0 8px 26px rgba(0,0,0,.08)}
.benefit p{position:absolute;right:110px;top:13px;width:450px;text-align:right;font-size:13px;line-height:19px;color:#5b5b5b}
.benefit-arrow{position:absolute;left:529px;top:-5px;width:68px;height:68px;border-radius:50%;background:var(--teal);border:5px solid #e2e8e8;display:flex;align-items:center;justify-content:center}

/* testimonials */
.testimonials-title{top:3232px}
.testimonials-glow{left:60px;top:3340px;width:1080px;height:340px;background:radial-gradient(ellipse at center,rgba(0,0,0,.06),rgba(0,0,0,0) 70%)}
.review{position:absolute;top:3417px;width:278px;height:191px;background:var(--white);box-shadow:0 4px 18px rgba(0,0,0,.06);text-align:center}
.review-avatar{position:absolute;left:94px;top:-45px;width:90px;height:90px;border-radius:50%;background:radial-gradient(circle at 50% 40%,#d9c2a8,#a9917a)}
.review-stars{position:absolute;left:0;top:68px;width:100%;display:flex;justify-content:center;gap:6px}
.review p{position:absolute;left:24px;top:110px;width:230px;font-size:8.5px;line-height:13px;color:#7a7a7a}
.review h4{position:absolute;left:0;top:157px;width:100%;font-size:12px;font-weight:600;color:var(--purple)}
.dots{left:583px;top:3634px;display:flex;gap:4px}
.dots span{width:20px;height:20px;border-radius:50%;background:var(--teal)}
.dots span.off{background:var(--white);border:2px solid var(--teal)}

/* footer */
.footer{left:0;top:3760px;width:1200px;height:546px;background:var(--beige)}
.footer-wave{left:0;top:3740px;width:1200px;height:140px}
.footer-badge{left:74px;top:3952px;width:156px;height:156px;border-radius:50%;background:var(--teal);border:5px solid var(--purple);display:flex;align-items:center;justify-content:center;text-align:center;color:var(--white);font-size:13px;font-weight:600;line-height:1.25;padding:18px}
.social{position:absolute;top:4132px;width:22px;height:22px;border-radius:50%;border:2px solid var(--purple)}
.col-title{position:absolute;font-size:23px;font-weight:600;color:var(--teal)}
.link-list{position:absolute;list-style:none;font-size:16px;color:#3a3a3a}
.link-list li{height:37px;display:flex;align-items:center;gap:10px}
.link-list li::before{content:"→";font-size:13px;color:#3a3a3a}
.contact-item{position:absolute;left:922px;display:flex;align-items:center;gap:14px;font-size:15px;color:#3a3a3a}
.footer-rule{left:209px;top:4238px;width:802px;height:1px;background:#a6988a}
.copyright{left:0;top:4262px;width:1200px;text-align:center;font-size:12px;color:#3a3a3a}
</style>
</head>
<body>

<!-- Hero -->
<div class="abs hero"></div>
<svg class="abs hero-wave" viewBox="0 0 1200 160" preserveAspectRatio="none">
  <path d="M0 135 C250 60 520 20 760 30 C950 40 1100 80 1200 115 L1200 160 L0 160 Z" fill="#fff"/>
  <path d="M480 40 C650 5 880 10 1200 115 L1200 140 C1050 80 900 45 760 30 C660 25 560 30 480 40 Z" fill="var(--purple)"/>
</svg>
<div class="abs brand-badge">MARIGOLD COVENANT</div>
<nav class="abs nav">
  <span style="left:279px">HOME</span>
  <span style="left:379px">ABOUT</span>
  <span style="left:493px">SERVICES</span>
  <span style="left:632px">TESTIMONIALS</span>
  <span style="left:759px">BLOG</span>
  <span style="left:866px">CONTACT</span>
</nav>
<a class="btn nav-cta">FREE CONSULTATION</a>
<h1 class="abs hero-title">TRANSFORMATIVE NEW LIFE AND INTIMACY COACHING COMPANY</h1>
<a class="btn hero-cta">FREE CONSULTATION</a>
<svg class="abs hero-arrow" style="left:72px;top:313px" viewBox="0 0 24 30"><path d="M17 4 L7 15 L17 26" fill="none" stroke="var(--teal)" stroke-width="3"/></svg>
<svg class="abs hero-arrow" style="left:1104px;top:333px" viewBox="0 0 24 30"><path d="M7 4 L17 15 L7 26" fill="none" stroke="var(--teal)" stroke-width="3"/></svg>
<div class="abs hero-photo" role="img" aria-label="Woman with red hair stretching in a sunlit lavender field"></div>

<!-- Services -->
<h2 class="section-title accent" style="top:700px">OUR SERVICES</h2>
<div class="service" style="left:172px;top:876px">
  <div class="service-icon"><svg width="44" height="44" viewBox="0 0 44 44" fill="none" stroke="#fff" stroke-width="2"><rect x="7" y="8" width="30" height="20" rx="2"/><path d="M3 32 H41 L38 36 H6 Z"/><circle cx="22" cy="16" r="4"/></svg></div>
  <h3>ONLINE COACHING</h3>
  <p>The sun dipped below the horizon, casting a warm golden glow across the tranquil waters of the lake.</p>
</div>
<div class="service" style="left:453px;top:876px">
  <div class="service-icon"><svg width="44" height="44" viewBox="0 0 44 44" fill="none" stroke="#fff" stroke-width="2"><rect x="9" y="6" width="22" height="30" rx="2"/><path d="M14 14 H26 M14 20 H26 M14 26 H20"/><circle cx="31" cy="32" r="6"/></svg></div>
  <h3>NUTRITION COACHING</h3>
  <p>The sun dipped below the horizon, casting a warm golden glow across the tranquil waters of the lake.</p>
</div>
<div class="service" style="left:732px;top:874px">
  <div class="service-icon"><svg width="44" height="44" viewBox="0 0 44 44" fill="none" stroke="#fff" stroke-width="2"><path d="M6 22 C6 14 14 12 18 18 C22 12 30 14 30 22 C30 28 18 34 18 34 C18 34 6 28 6 22 Z"/><path d="M9 22 H14 L16 18 L19 26 L21 22 H26"/><circle cx="35" cy="9" r="3"/></svg></div>
  <h3>, LIFESTYLE COACHING</h3>
  <p>The sun dipped below the horizon, casting a warm golden glow across the tranquil waters of the lake.</p>
</div>
<div class="service" style="left:1021px;top:874px">
  <div class="service-icon"><svg width="44" height="44" viewBox="0 0 44 44" fill="none" stroke="#fff" stroke-width="2"><rect x="8" y="28" width="28" height="8"/><path d="M8 28 V20 H18 V28 M26 28 V12 H36 V28"/><circle cx="13" cy="14" r="3"/><circle cx="31" cy="7" r="3"/></svg></div>
  <h3>, SPECIALTY PROGRAMS</h3>
  <p>The sun dipped below the horizon, casting a warm golden glow across the tranquil waters of the lake.</p>
</div>

<!-- About -->
<div class="abs about-frame"></div>
<div class="abs about-photo" role="img" aria-label="Woman with outstretched arms standing in a grassy field under a pale sky"></div>
<h2 class="abs about-title">ABOUT <span class="accent">US</span></h2>
<p class="abs about-text">The sun dipped below the horizon, casting a warm golden glow across the tranquil waters of the lake. Birds chirped softly as a gentle breeze rustled the leaves of the nearby trees. In the distance, a small boat drifted lazily, its oars cutting through the glassy surface with soft ripples.</p>
<a class="btn about-cta">READ MORE</a>

<!-- Featured programs -->
<div class="abs featured" role="img" aria-label="Faded photo of a woman with open arms in a meadow"></div>
<h2 class="section-title featured-title">FEATURED <span class="accent">PROGRAMS</span></h2>
<p class="abs featured-sub">The sun dipped below the horizon, casting a warm golden glow across the tranquil waters of the lake.</p>
<div class="abs phone-circle"><svg width="40" height="40" viewBox="0 0 24 24"><path d="M6.6 10.8a15 15 0 0 0 6.6 6.6l2.2-2.2a1 1 0 0 1 1-.25 11.4 11.4 0 0 0 3.6.6 1 1 0 0 1 1 1V20a1 1 0 0 1-1 1A17 17 0 0 1 3 4a1 1 0 0 1 1-1h3.5a1 1 0 0 1 1 1c0 1.25.2 2.45.6 3.6a1 1 0 0 1-.25 1Z" fill="#fff"/></svg></div>
<div class="abs help-label">Need Help Now?</div>
<div class="abs help-call">Call : 1 555 014 2290</div>
<div class="abs or-word">or</div>
<a class="btn featured-cta">FREE CONSULTATION</a>

<!-- Key benefits -->
<h2 class="section-title benefits-title">KEY <span class="accent">BENEFITS</span></h2>
<p class="abs benefits-sub">The sun dipped below the horizon, casting a warm golden glow across the tranquil waters of the lake.</p>
<div class="abs benefits-photo" role="img" aria-label="Joyful woman in a knit top running through a field"></div>
<div class="benefit" style="top:2599px"><p>helping individuals foster deeper relationships, self-awareness, and life satisfaction.</p><div class="benefit-arrow"><svg width="34" height="34" viewBox="0 0 34 34" fill="none" stroke="#fff" stroke-width="2.5"><circle cx="17" cy="17" r="14"/><path d="M10 17 H23 M18 12 L23 17 L18 22"/></svg></div></div>
<div class="benefit" style="top:2706px"><p>helping individuals foster deeper relationships, self-awareness, and life satisfaction.</p><div class="benefit-arrow"><svg width="34" height="34" viewBox="0 0 34 34" fill="none" stroke="#fff" stroke-width="2.5"><circle cx="17" cy="17" r="14"/><path d="M10 17 H23 M18 12 L23 17 L18 22"/></svg></div></div>
<div class="benefit" style="top:2820px"><p>helping individuals foster deeper relationships, self-awareness, and life satisfaction.</p><div class="benefit-arrow"><svg width="34" height="34" viewBox="0 0 34 34" fill="none" stroke="#fff" stroke-width="2.5"><circle cx="17" cy="17" r="14"/><path d="M10 17 H23 M18 12 L23 17 L18 22"/></svg></div></div>
<div class="benefit" style="top:2927px"><p>helping individuals foster deeper relationships, self-awareness, and life satisfaction.</p><div class="benefit-arrow"><svg width="34" height="34" viewBox="0 0 34 34" fill="none" stroke="#fff" stroke-width="2.5"><circle cx="17" cy="17" r="14"/><path d="M10 17 H23 M18 12 L23 17 L18 22"/></svg></div></div>

<!-- Testimonials -->
<h2 class="section-title testimonials-title">WHAT CLIENT <span class="accent">SAYS</span></h2>
<div class="abs testimonials-glow"></div>
<div class="review" style="left:130px">
  <div class="review-avatar" role="img" aria-label="Client portrait"></div>
  <div class="review-stars"><svg width="110" height="18" viewBox="0 0 110 18" fill="var(--teal)"><path id="st" d="M9 0l2.6 5.8 6.4.6-4.8 4.2 1.4 6.3L9 13.6 3.4 16.9l1.4-6.3L0 6.4l6.4-.6Z"/><use href="#st" x="23"/><use href="#st" x="46"/><use href="#st" x="69"/><use href="#st" x="92"/></svg></div>
  <p>Lorem ipsum dolor sit amet, consectetur adipiscing elit, sed do eiusmodtempor incididunt ut labore et dolore magna aliqua. Ut enim ad minim</p>
  <h4>JOHN DOE</h4>
</div>
<div class="review" style="left:473px">
  <div class="review-avatar" role="img" aria-label="Client portrait"></div>
  <div class="review-stars"><svg width="110" height="18" viewBox="0 0 110 18" fill="var(--teal)"><use href="#st"/><use href="#st" x="23"/><use href="#st" x="46"/><use href="#st" x="69"/><use href="#st" x="92"/></svg></div>
  <p>Lorem ipsum dolor sit amet, consectetur adipiscing elit, sed do eiusmodtempor incididunt ut labore et dolore magna aliqua. Ut enim ad minim</p>
  <h4>JOHN DOE</h4>
</div>
<div class="review" style="left:815px">
  <div class="review-avatar" role="img" aria-label="Client portrait"></div>
  <div class="review-stars"><svg width="110" height="18" viewBox="0 0 110 18" fill="var(--teal)"><use href="#st"/><use href="#st" x="23"/><use href="#st" x="46"/><use href="#st" x="69"/><use href="#st" x="92"/></svg></div>
  <p>Lorem ipsum dolor sit amet, consectetur adipiscing elit, sed do eiusmodtempor incididunt ut labore et dolore magna aliqua. Ut enim ad minim</p>
  <h4>JOHN DOE</h4>
</div>
<div class="abs dots"><span></span><span class="off"></span><span></span></div>

<!-- Footer -->
<div class="abs footer"></div>
<svg class="abs footer-wave" viewBox="0 0 1200 140" preserveAspectRatio="none">
  <path d="M0 0 H1200 V10 C1000 90 700 120 500 115 C300 110 120 70 0 40 Z" fill="#fff"/>
  <path d="M0 14 C140 60 320 100 500 112 C720 125 980 80 1200 0 V14 C980 95 720 132 500 122 C320 112 140 72 0 32 Z" fill="var(--purple)"/>
</svg>
<div class="abs footer-badge">MARIGOLD COVENANT</div>
<span class="social" style="left:86px" role="img" aria-label="Social profile"></span>
<span class="social" style="left:143px" role="img" aria-label="Social profile"></span>
<span class="social" style="left:200px" role="img" aria-label="Social profile"></span>

<h3 class="col-title" style="left:369px;top:3962px">COMPANY</h3>
<ul class="link-list" style="left:378px;top:4011px"><li>Home</li><li>About</li><li>Services</li><li>Blog</li><li>Contact</li></ul>

<h3 class="col-title" style="left:615px;top:3962px">QUICK LINKS</h3>
<ul class="link-list" style="left:636px;top:4019px"><li>Pricing</li><li>Get Started</li><li>Privacy Policy</li><li>Client Login</li><li>Terms &amp; Conditions</li></ul>

<h3 class="col-title" style="left:922px;top:3966px">CONTACT</h3>
<div class="contact-item" style="top:4036px"><svg width="20" height="20" viewBox="0 0 24 24"><path d="M6.6 10.8a15 15 0 0 0 6.6 6.6l2.2-2.2a1 1 0 0 1 1-.25 11.4 11.4 0 0 0 3.6.6 1 1 0 0 1 1 1V20a1 1 0 0 1-1 1A17 17 0 0 1 3 4a1 1 0 0 1 1-1h3.5a1 1 0 0 1 1 1c0 1.25.2 2.45.6 3.6a1 1 0 0 1-.25 1Z" fill="var(--purple)"/></svg>1-555-019-3382</div>
<div class="contact-item" style="top:4085px"><svg width="20" height="20" viewBox="0 0 24 24"><rect x="2" y="5" width="20" height="14" rx="2" fill="var(--purple)"/><path d="M3 6 L12 13 L21 6" fill="none" stroke="#fff" stroke-width="1.6"/></svg>hello@marigoldcovenant.com</div>
<div class="contact-item" style="top:4132px"><svg width="20" height="22" viewBox="0 0 24 26"><path d="M12 1a8 8 0 0 0-8 8c0 6 8 16 8 16s8-10 8-16a8 8 0 0 0-8-8Z" fill="var(--purple)"/><circle cx="12" cy="9" r="3" fill="var(--beige)"/></svg>12 Orchard Lane, Fairhaven</div>

<div class="abs footer-rule"></div>
<p class="abs copyright">Privacy Policy | © Copyright 2024, All Rights Reserved.</p>

</body>
</html>
```